Business Card Design

chiropractor. Searching for a fresh cool look. Tired of all the run of the mill designs. I am open tocolors and all new designs..

Target Market(s)

auto accidents workers compensation and private insurance

Industry/Entity Type

Business

Contact Information for Business Card

Dr. Mark S. Snyder193-02 northern blvd.Flushing, new york 11358Upper level rear suitephone 718 224 3605fax 718 640 1837

Font styles to use
Sans Serif

Requirements
Must have
• my office hours on back of card
• monday 9am-noon; 2:30pm-7pm
• tuesday 2:30pm-7pm
• wednesday 9am-noon; 2;30pm-7pm
• thursday 4pm-7pm
• friday4pm-7pm
Nice to have
• some kind of real cool logo

```html
<!DOCTYPE html>
<html lang="en">
<head>
<meta charset="utf-8">
<title>Dr. Paul T. Wexham – Business Card</title>
<link href="https://fonts.googleapis.com/css2?family=Arimo:wght@400;700&display=swap" rel="stylesheet">
<style>
  :root {
    --page-bg: #e9ecef;
    --card-white: #ffffff;
    --card-blue: #0a9ee2;
    --card-blue-deep: #1a78c9;
    --navy: #1c2340;
    --ink: #1f2433;
    --text-white: #ffffff;
    --bone-peach: #f3c9a8;
    --mist: #dfe3ea;
  }
  * { box-sizing: border-box; margin: 0; padding: 0; }
  html, body {
    width: 1200px; height: 900px; overflow: hidden;
    background: var(--page-bg);
    font-family: "Arimo", Arial, sans-serif;
  }
  .canvas {
    width: 1200px; height: 900px;
    display: flex; flex-direction: column;
    align-items: center; justify-content: center; gap: 30px;
  }
  .card {
    position: relative; width: 720px; height: 411px;
    overflow: hidden;
    box-shadow: 0 10px 28px rgba(20, 30, 50, 0.22);
  }

  /* Back side: office hours */
  .card--back { background: var(--card-white); }
  .back-figure {
    position: absolute; left: 0; top: 0; width: 300px; height: 100%;
    background:
      radial-gradient(ellipse 60px 150px at 150px 190px, rgba(243, 201, 168, 0.75), transparent 70%),
      radial-gradient(ellipse 180px 260px at 120px 220px, var(--mist), transparent 75%),
      linear-gradient(90deg, #e6e9ef 0%, #f4f5f8 70%, rgba(255,255,255,0) 100%);
  }
  .hours {
    position: absolute; left: 235px; top: 86px; width: 420px;
  }
  .hours__title {
    display: inline-block; margin-left: 45px; margin-bottom: 26px;
    background: var(--navy); color: var(--text-white);
    font-size: 15px; letter-spacing: 0.5px;
    padding: 4px 30px;
  }
  .hours__row {
    display: flex; align-items: baseline;
    color: var(--ink); font-size: 18px; line-height: 1; margin-bottom: 18px;
  }
  .hours__day { white-space: nowrap; }
  .hours__leader {
    flex: 0 0 auto; width: 70px; margin: 0 3px;
    border-bottom: 2px dotted var(--ink); transform: translateY(-3px);
  }
  .hours__leader--short { width: 45px; }
  .hours__leader--long { width: 90px; }
  .hours__time { white-space: nowrap; }

  /* Front side: identity */
  .card--front { background: var(--card-blue); color: var(--text-white); }
  .front-figure {
    position: absolute; right: 0; top: 0; width: 420px; height: 100%;
    background:
      radial-gradient(ellipse 70px 190px at 210px 200px, rgba(20, 80, 150, 0.55), transparent 75%),
      radial-gradient(ellipse 220px 260px at 230px 190px, rgba(30, 100, 190, 0.55), transparent 75%),
      linear-gradient(90deg, rgba(10,158,226,0) 0%, var(--card-blue-deep) 100%);
  }
  .identity { position: absolute; left: 68px; top: 92px; }
  .identity__name {
    font-size: 27px; font-weight: 700; text-transform: uppercase; letter-spacing: 0.3px;
  }
  .identity__role { font-size: 20px; margin-top: 6px; }
  .contact {
    position: absolute; left: 90px; top: 262px; list-style: none;
    font-size: 18px; line-height: 1.2;
  }
  .contact__item { display: flex; align-items: flex-start; gap: 16px; margin-bottom: 4px; }
  .contact__icon { width: 20px; height: 20px; flex: 0 0 20px; margin-top: 1px; }
</style>
</head>
<body>
<main class="canvas">

  <section class="card card--back" aria-label="Card back: office hours">
    <div class="back-figure" role="img" aria-label="Faint anatomical illustration of the upper back and spine"></div>
    <div class="hours">
      <div class="hours__title">OFFICE TIME</div>
      <div class="hours__row"><span class="hours__day">Monday</span><span class="hours__leader"></span><span class="hours__time">9am-noon; 2:30pm-7pm</span></div>
      <div class="hours__row"><span class="hours__day">Tuesday</span><span class="hours__leader"></span><span class="hours__time">2:30pm-7pm</span></div>
      <div class="hours__row"><span class="hours__day">Wednesday</span><span class="hours__leader hours__leader--short"></span><span class="hours__time">9am-noon; 2:30pm-7pm</span></div>
      <div class="hours__row"><span class="hours__day">Thursday</span><span class="hours__leader"></span><span class="hours__time">4pm-7pm</span></div>
      <div class="hours__row"><span class="hours__day">Friday</span><span class="hours__leader hours__leader--long"></span><span class="hours__time">4pm-7pm</span></div>
    </div>
  </section>

  <section class="card card--front" aria-label="Card front: contact details">
    <div class="front-figure" role="img" aria-label="Blue anatomical illustration of a torso showing the spine and rib cage"></div>
    <div class="identity">
      <h1 class="identity__name">Dr. Paul T. Wexham</h1>
      <p class="identity__role">Chiropractor</p>
    </div>
    <ul class="contact">
      <li class="contact__item">
        <svg class="contact__icon" viewBox="0 0 20 20" aria-hidden="true">
          <rect width="20" height="20" rx="4" fill="#fff"/>
          <path d="M6 4.5c.6-.4 1.3-.2 1.6.4l1 1.9c.3.5.1 1.1-.3 1.4l-.9.6c.5 1.3 1.5 2.4 2.8 3l.6-.9c.3-.5.9-.6 1.4-.3l1.9 1c.6.3.8 1 .4 1.6l-.7 1c-.5.7-1.4 1-2.2.7C8.3 13.8 6.2 11.7 5 8.4c-.3-.8 0-1.7.7-2.2z" fill="var(--card-blue)"/>
        </svg>
        <span>718 506 8412</span>
      </li>
      <li class="contact__item">
        <svg class="contact__icon" viewBox="0 0 20 20" aria-hidden="true">
          <rect width="20" height="20" rx="4" fill="#fff"/>
          <rect x="6" y="3.5" width="8" height="4" fill="var(--card-blue)"/>
          <rect x="3.5" y="8" width="13" height="6" rx="1" fill="var(--card-blue)"/>
          <rect x="6" y="12" width="8" height="4.5" fill="#fff" stroke="var(--card-blue)" stroke-width="1.2"/>
        </svg>
        <span>718 640 1837</span>
      </li>
      <li class="contact__item">
        <svg class="contact__icon" viewBox="0 0 20 20" aria-hidden="true">
          <rect width="20" height="20" rx="4" fill="#fff"/>
          <path d="M10 3.5a4.5 4.5 0 0 0-4.5 4.5c0 3.3 4.5 8.5 4.5 8.5s4.5-5.2 4.5-8.5A4.5 4.5 0 0 0 10 3.5z" fill="var(--card-blue)"/>
          <circle cx="10" cy="8" r="1.7" fill="#fff"/>
        </svg>
        <span>487-16 linden ave.Flushing,<br>New york 11472<br>Upper level rear suite</span>
      </li>
    </ul>
  </section>

</main>
</body>
</html>
```